Law Firm Ad

We need a magazine/auction program design for a Sacramento based law firm. Current need is for a school auction sponsorship. Ad must be 5 1/2 x 8 1/2 in high resolution (300 dpi) and in JPG or PDF format. A clean, modern, simple design is preferred.

Brisley Law Corporation provides general preventative employment advice to employers in avoiding litigation and has counseled businesses on cases involving employment law, unfair business practices and trade secrets. Brisley Law Corporation also practices in business, real estate and employment litigation.

Target Market(s)

This particular ad it is to support Hollowbrook Elementary School's 21st Annual Auction and Dinner on March 14, 2015.
Here's the facebook link https://www.examplesocial.net/HollowbrookAuction/photos/a.718204936051827.260319.709482615039471/2049361857402116/?type=1&theater
But I would like something that might be fairly universal.

Industry/Entity Type

Real Estate

Font styles to use
Sans Serif

Requirements
Must have
• Clean and crisp design. Not overly traditional.
Nice to have
• Contact information:
Brisley Law Corporation
388 Wexley Avenue, Suite 200
Sacramento, CA 95871
916.555.0147
brisley-law.example

```html
<!DOCTYPE html>
<html lang="en">
<head>
<meta charset="utf-8">
<title>Brisley Law Corporation – Sponsorship Ad</title>
<link rel="stylesheet" href="https://fonts.googleapis.com/css2?family=Montserrat:wght@600&family=Cabin:wght@400&display=swap">
<style>
  :root {
    --stage: #121212;
    --paper: #ffffff;
    --ink: #231f20;
    --yellow-text: #fff23d;
    --orange-text: #ffb52e;
    --red: #e5232e;
  }
  * { margin: 0; padding: 0; box-sizing: border-box; }
  html, body {
    width: 1200px; height: 1000px; overflow: hidden;
    background: var(--stage);
  }
  .ad {
    position: absolute;
    left: 306px; top: 68px;
    width: 556px; height: 847px;
    background: var(--paper);
    padding: 12px 11px 10px 11px;
  }
  .ad-art { display: block; width: 533px; height: 825px; }
  .brand-name { font-family: "Montserrat", sans-serif; font-weight: 600; fill: var(--ink); text-anchor: middle; }
  .panel-title { font-family: "Cabin", sans-serif; font-weight: 400; letter-spacing: 1px; }
  .contact { font-family: "Cabin", sans-serif; fill: var(--paper); text-anchor: middle; }
</style>
</head>
<body>
  <div class="ad">
    <svg class="ad-art" viewBox="0 0 533 825" xmlns="http://www.w3.org/2000/svg">
      <defs>
        <linearGradient id="hero-tone" x1="0" y1="0" x2="1" y2="0.4">
          <stop offset="0" stop-color="#d9d2c4"/>
          <stop offset="0.3" stop-color="#e8c98e"/>
          <stop offset="0.55" stop-color="#d9b7a8"/>
          <stop offset="0.75" stop-color="#8fbf83"/>
          <stop offset="1" stop-color="#dcd8cc"/>
        </linearGradient>
        <linearGradient id="hero-fade" x1="0" y1="0" x2="0" y2="1">
          <stop offset="0.7" stop-color="#ffffff" stop-opacity="0"/>
          <stop offset="1" stop-color="#ffffff" stop-opacity="0.9"/>
        </linearGradient>
        <linearGradient id="yellow-tone" x1="0" y1="0" x2="0" y2="1">
          <stop offset="0" stop-color="#f39b1a"/>
          <stop offset="1" stop-color="#f7b416"/>
        </linearGradient>
        <linearGradient id="orange-tone" x1="0" y1="0" x2="0" y2="1">
          <stop offset="0" stop-color="#ee6a1e"/>
          <stop offset="1" stop-color="#f18424"/>
        </linearGradient>
      </defs>

      <!-- hero photo area -->
      <rect x="0" y="0" width="533" height="360" fill="url(#hero-tone)" role="img" aria-label="Photo of young children painting at a classroom table"/>
      <rect x="0" y="0" width="533" height="360" fill="url(#hero-fade)"/>

      <!-- brand triangle -->
      <polygon points="0,335 533,335 263,582" fill="var(--paper)"/>

      <!-- side panels -->
      <polygon points="0,335 263,582 0,825" fill="url(#yellow-tone)" stroke="var(--paper)" stroke-width="2" role="img" aria-label="Yellow-toned photo of a young child playing"/>
      <polygon points="533,335 263,582 533,825" fill="url(#orange-tone)" stroke="var(--paper)" stroke-width="2" role="img" aria-label="Orange-toned photo of a hand dropping a coin into a piggy bank"/>
      <!-- contact panel -->
      <polygon points="10,825 263,582 523,825" fill="var(--red)" stroke="var(--paper)" stroke-width="2"/>

      <!-- brand -->
      <text class="brand-name" x="263" y="412" font-size="56">Brisley</text>
      <text class="brand-name" x="263" y="455" font-size="19" letter-spacing="1.5" fill="#58595b">LAW CORPORATION</text>

      <!-- panel titles -->
      <text class="panel-title" transform="translate(8,386) rotate(43)" font-size="36" fill="var(--yellow-text)">ELEMENTARY</text>
      <text class="panel-title" transform="translate(2,430) rotate(43)" font-size="36" fill="#ffffff" fill-opacity="0.4">SCHOOL</text>

      <text class="panel-title" transform="translate(318,606) rotate(-43)" font-size="36" fill="var(--orange-text)" fill-opacity="0.6">FUNDING</text>
      <text class="panel-title" transform="translate(336,646) rotate(-43)" font-size="36" fill="var(--orange-text)">PROGRAM</text>

      <!-- contact -->
      <text class="contact" x="266" y="756" font-size="19" letter-spacing="0.6">BRISLEY LAW CORPORATION</text>
      <text class="contact" x="266" y="774" font-size="15">388 Wexley Avenue, Suite 200</text>
      <text class="contact" x="266" y="791" font-size="15">Sacramento, CA 95871</text>
      <text class="contact" x="266" y="808" font-size="15">916.555.0147 &#160;&#160;|&#160;&#160; brisley-law.example</text>
    </svg>
  </div>
</body>
</html>
```